Valentine's Day Flyer

We require an A5 size flyer to promote our February parking offer & Giveaway.

Offer:
Book your parking online & Save!
$5 Night/Weekend Parking
$10 Early Bird Parking

Giveaway: Win a $5,000 Diamond Ring!
Every time you book your parking online using Trundle-Nook you get a chance to win!

The final design should contain:
- Valentine's Theme
- Emphasise 'Book your parking online & Save!'

Designers: please visit www.halvorbaypark.com.au for more info on Halvor Bay Parking & Trundle-Nook

Target Market(s)

18-50 year old drivers

Industry/Entity Type

Parking

```html
<!DOCTYPE html>
<html lang="en">
<head>
<meta charset="utf-8">
<title>Trundle-Nook Valentine's Day Flyer</title>
<link href="https://fonts.googleapis.com/css2?family=Oswald:wght@500;700&family=Great+Vibes&display=swap" rel="stylesheet">
<style>
  :root {
    --red-deep: #7d0a12;
    --red-main: #b8121d;
    --red-glow: #d82a2f;
    --panel: rgba(255, 170, 170, 0.22);
    --ink-dark: #2b1212;
    --white: #ffffff;
    --brand-blue: #0c5aa6;
    --photo-light: #c9545a;
    --photo-dark: #9e1820;
  }
  html, body {
    margin: 0;
    padding: 0;
    overflow: hidden;
    background: var(--white);
  }
  .flyer {
    position: relative;
    width: 853px;
    height: 1200px;
    overflow: hidden;
    background: var(--white);
    font-family: "Oswald", "Arial Narrow", sans-serif;
  }
  .hero {
    position: absolute;
    left: 0;
    top: 0;
    width: 853px;
    height: 945px;
    background: radial-gradient(ellipse at 70% 45%, var(--red-glow) 0%, var(--red-main) 45%, var(--red-deep) 100%);
    overflow: hidden;
  }
  .photo {
    position: absolute;
    left: 470px;
    top: 250px;
    width: 383px;
    height: 695px;
    background: linear-gradient(180deg, var(--photo-dark) 0%, var(--photo-light) 40%, var(--photo-light) 75%, var(--photo-dark) 100%);
  }
  .headline {
    position: absolute;
    left: 0;
    top: 30px;
    width: 853px;
    margin: 0;
    text-align: center;
    color: var(--white);
    font-weight: 500;
    font-size: 72px;
    line-height: 1;
    letter-spacing: 1px;
  }
  .headline em {
    font-style: italic;
  }
  .occasion {
    position: absolute;
    right: 40px;
    top: 148px;
    margin: 0;
    color: var(--white);
    font-family: "Great Vibes", cursive;
    font-size: 60px;
    line-height: 1;
  }
  .offer-panel {
    position: absolute;
    left: 40px;
    top: 242px;
    width: 358px;
    height: 470px;
    border-radius: 14px;
    background: var(--panel);
  }
  .offer-text {
    position: absolute;
    right: 20px;
    top: 14px;
    margin: 0;
    text-align: right;
    color: var(--ink-dark);
    font-weight: 700;
    font-size: 74px;
    line-height: 0.98;
    text-transform: uppercase;
  }
  .offer-text .save {
    display: block;
    color: var(--white);
    font-size: 100px;
    line-height: 1.05;
  }
  .giveaway-band {
    position: absolute;
    left: -60px;
    top: 703px;
    width: 980px;
    height: 104px;
    background: var(--white);
    transform: rotate(-9deg);
    transform-origin: center top;
    text-align: center;
    color: var(--red-main);
  }
  .giveaway-title {
    margin: 10px 0 0;
    font-weight: 700;
    font-size: 50px;
    line-height: 1.05;
    letter-spacing: 1px;
  }
  .giveaway-detail {
    margin: 0;
    font-weight: 500;
    font-size: 18px;
    line-height: 1.2;
    letter-spacing: 0.3px;
  }
  .brand {
    position: absolute;
    left: 16px;
    top: 960px;
    display: flex;
    align-items: center;
    gap: 28px;
  }
  .brand-mark {
    width: 230px;
    height: 220px;
    background: var(--brand-blue);
  }
  .brand-name {
    margin: 0;
    color: var(--brand-blue);
    font-weight: 700;
    font-size: 58px;
    line-height: 1.05;
  }
</style>
</head>
<body>
  <main class="flyer">
    <section class="hero">
      <div class="photo" role="img" aria-label="Photo of two fingers with drawn smiles hugging, a red heart between them"></div>
      <h1 class="headline">TRUNDLE-<em>YOUR</em>-NOOK</h1>
      <p class="occasion">this Valentines Day</p>
      <div class="offer-panel">
        <p class="offer-text">Book<br>your<br>parking<br>online<br>and<span class="save">Save!</span></p>
      </div>
    </section>
    <div class="giveaway-band">
      <p class="giveaway-title">WIN A $5,000 DIAMOND RING!</p>
      <p class="giveaway-detail">EVERY TIME YOU BOOK YOUR PARKING ONLINE USING TRUNDLE-NOOK YOU GET A CHANCE TO WIN!</p>
    </div>
    <footer class="brand">
      <div class="brand-mark"></div>
      <p class="brand-name">Halvor Bay<br>Parking</p>
    </footer>
  </main>
</body>
</html>
```